Brochure Design Project

This will be a tri-fold full 8.5x11 brochure that will be distributed and sitting in Oncology offices all throughout the US. It is a lead generation and referral designed piece that it to target all patients, Cancer primarily, but all critically ill patients and seniors above the age of 70. We want our service to go beyond just a financial transaction, we want to educate patients of their rights within a life insurance policy and if we cannot help them personally, do want to assist them by referring them to other agencies and non profits than can. ( I want to redesign the brochure attached, it can be very similar and need only minor changes to content, but would welcome all suggestions on improving message, and in gaining attention, picture substitutions and change of colors, along with the layout itself can be improved upon, and I need this piece to look very professional and appropriate for medical offices. I will be needing assistance on several upcoming projects and will also have great printing demands.

Target Market(s)

Cancer patients
all chronically and critically ill patients
all seniors above age 70

Industry/Entity Type

Life Insurance

Requirements
Must have
• Cancer and the terminally ill
Nice to have
• seniors above 70

```html
<!DOCTYPE html>
<html lang="en">
<head>
<meta charset="utf-8">
<title>Lumen Settlements – Tri-fold Brochure</title>
<link href="https://fonts.googleapis.com/css2?family=Tinos:ital,wght@0,400;0,700;1,400;1,700&family=Libre+Baskerville:wght@700&display=swap" rel="stylesheet">
<style>
  :root {
    --paper: #eef6f8;
    --ink: #1f1f1f;
    --green: #3f6a2c;
    --frame: #2a2a2a;
  }
  * { margin: 0; padding: 0; box-sizing: border-box; }
  html, body {
    width: 1200px; height: 925px; overflow: hidden;
    background: var(--paper);
  }
  body {
    position: relative;
    font-family: "Tinos", "Times New Roman", serif;
    color: var(--ink);
  }
  .panel { position: absolute; top: 0; height: 925px; }
  .panel--left { left: 22px; width: 345px; }
  .panel--middle { left: 420px; width: 360px; }
  .panel--right { left: 815px; width: 360px; text-align: center; }

  .facts-title {
    position: absolute; top: 34px; left: 22px;
    font-size: 21px; font-weight: 400; text-decoration: underline;
    text-underline-offset: 3px;
  }
  .fact { position: absolute; left: 0; font-size: 20.5px; line-height: 22.5px; }
  .fact--one { top: 86px; left: 6px; }
  .fact--two { top: 205px; }
  .fact--three { top: 320px; }

  .promise {
    position: absolute; left: 4px;
    font-size: 20.5px; line-height: 26px; font-style: italic;
    letter-spacing: 0.2px;
  }
  .promise strong { font-weight: 700; }
  .promise--one { top: 540px; text-indent: 36px; }
  .promise--two { top: 700px; text-indent: 36px; }

  .headline {
    position: absolute; top: 34px; left: 0; width: 100%; text-align: center;
    font-family: "Libre Baskerville", "Times New Roman", serif;
    font-size: 21px; font-weight: 700;
  }
  .subhead {
    position: absolute; top: 72px; left: 0; width: 100%; text-align: center;
    font-size: 23.5px; line-height: 25px; letter-spacing: 0.3px;
  }
  .photo-frame {
    position: absolute; top: 193px; left: 9px; width: 343px; height: 418px;
    border: 1.5px solid var(--frame);
    display: flex; align-items: center; justify-content: center;
  }
  .photo-frame span {
    font-family: "Libre Baskerville", "Times New Roman", serif;
    font-size: 23px; font-weight: 700; margin-top: -10px;
  }

  .eligibility {
    position: absolute; top: 32px; left: 0; width: 100%;
    font-size: 20.5px; line-height: 23px; text-align: left; padding-left: 8px;
  }
  .eligibility-title {
    position: absolute; top: 200px; left: 0; width: 100%;
    font-family: "Libre Baskerville", "Times New Roman", serif;
    color: var(--green); font-size: 22px; line-height: 26px; font-weight: 700;
  }
  .eligibility-title .big { font-size: 23px; letter-spacing: 1px; }
  .call-text {
    position: absolute; top: 332px; left: 0; width: 100%;
    font-size: 20.5px; line-height: 25.5px;
  }
  .phone {
    position: absolute; top: 537px; left: 0; width: 100%;
    font-family: "Libre Baskerville", "Times New Roman", serif;
    font-size: 22px; font-weight: 700;
  }
  .brand {
    position: absolute; top: 640px; left: 0; width: 100%;
    display: flex; flex-direction: column; align-items: center; gap: 14px;
  }
  .brand-dot { width: 44px; height: 44px; border-radius: 50%; background: var(--green); }
  .brand-name {
    font-family: "Tinos", "Times New Roman", serif;
    font-size: 34px; font-weight: 400; color: var(--ink); line-height: 1;
  }
  .website {
    position: absolute; top: 798px; left: 0; width: 100%;
    font-size: 20.5px; letter-spacing: 0.4px;
  }
</style>
</head>
<body>
  <section class="panel panel--left">
    <h2 class="facts-title">Some Facts To Consider</h2>
    <p class="fact fact--one">Many insurance companies<br>conceal the fact that policy<br>holders may be entitled to<br>additional cash benefits.</p>
    <p class="fact fact--two">Bankruptcy rates among<br>Cancer patients and seniors<br>are more than double the<br>general population.</p>
    <p class="fact fact--three">Most patients are unsure<br>about where to turn and what<br>questions they should be<br>asking about their financial<br>situtation and what options<br>are available.</p>
    <p class="promise promise--one"><strong>Everyone</strong> on the journey<br>of medical recovery should<br>have access to Financial<br>Support that improves<br>quality of life and provides<br>relief from distress.</p>
    <p class="promise promise--two"><strong>We Can Help</strong> provide the<br>information and guidance<br>you need to learn more about<br>the Financial Resources<br>available to you.</p>
  </section>

  <section class="panel panel--middle">
    <h1 class="headline">Healing and Recovery</h1>
    <p class="subhead">should be the primary<br>concern for all patients<br>“not money” or “lack of”</p>
    <div class="photo-frame" role="img" aria-label="Photo area: a patient and caregiver in a calm, hopeful medical setting">
      <span>insert image</span>
    </div>
  </section>

  <section class="panel panel--right">
    <p class="eligibility">If you were born before 1943<br>and have been diagnosed with<br>a life threatening illness and<br>own life insurance or you are<br>covered by a group policy...</p>
    <h2 class="eligibility-title">You May Be Eligible<br>To Receive a<br><span class="big">LUMEN SETTLEMENT</span></h2>
    <p class="call-text">Call today to receive a free<br>and confidential<br>Lumen Settlement Kit<br>or ask one of our<br>Family Service Counselors<br>for assistance or advice<br>on where to turn.</p>
    <p class="phone">1-800-555-0148</p>
    <div class="brand">
      <span class="brand-dot" aria-hidden="true"></span>
      <span class="brand-name">Lumen Settlements</span>
    </div>
    <p class="website">www.lumensettlements.com</p>
  </section>
</body>
</html>
```